Bright Owl Learning Centre website redesign

Our website (which we have only just converted to wordpress) is just not good enough for my liking. Our centre offers classes for babies aged from 6 months to 7 years old in the middle east. Whilst our program is formal in the way that the practise deals with learning in hemispheres of the brain - the site should look more fun and a bit more approachable and attractive to families.
I like the site www.tinyparade.example or www.plumvalley.example from this region - I like the way that you land on home page with images and a quote rather than all this information coming at you and you not knowing where to click.
I want a fun and appealing site that features info about the program, class timetable, shop, news and events, gallery, blog posts etc…
I am really open to a complete redesign and just want something that looks professional but is fun and gets the information out quickly! Please look at www.brightowl.example for current site design

```html
<!DOCTYPE html>
<html lang="en">
<head>
<meta charset="utf-8">
<title>Bright Owl Learning Centre</title>
<link href="https://fonts.googleapis.com/css2?family=Open+Sans:wght@400;600;700&display=swap" rel="stylesheet">
<style>
:root{
  --page-bg:#efe6dc;
  --sheet:#ffffff;
  --teal:#3f8aa6;
  --teal-dark:#2f7490;
  --orange:#f08a24;
  --ink:#555555;
  --ink-soft:#7a7a7a;
  --rule:#e2e2e2;
  --sand:#ece0d0;
  --cream:#fbf7e4;
  --footer:#333333;
  --footer-deep:#262626;
}
*{box-sizing:border-box;margin:0;padding:0}
html,body{width:1200px;height:2651px;overflow:hidden}
body{background:var(--page-bg);font-family:"Open Sans",Arial,sans-serif;color:var(--ink);position:relative}
a{color:inherit;text-decoration:none}
.abs{position:absolute}
.sheet{position:absolute;left:131px;top:0;width:936px;height:2324px;background:var(--sheet)}
.ph{display:block}
/* header */
.brand{left:148px;top:28px;display:flex;align-items:center;gap:10px}
.brand-mark{width:46px;height:46px;border-radius:50%;background:var(--teal)}
.brand-name{font-size:17px;font-weight:700;color:var(--teal);line-height:1.15;width:130px}
.toplinks{right:152px;top:28px;font-size:12px;color:#444;white-space:nowrap}
.toplinks span{padding:0 10px;border-left:1px solid #999}
.toplinks span:first-child{border-left:0}
.search{left:652px;top:68px;display:flex}
.search-field{width:198px;height:26px;border:1px solid #ddd;background:#f7f7f7;font-size:11px;color:#999;padding:5px 8px}
.search-btn{width:66px;height:26px;background:#555;color:#fff;font-size:13px;font-weight:600;text-align:center;line-height:26px}
.social{left:944px;top:67px;display:flex;gap:10px}
.social i{width:28px;height:28px;border-radius:50%;display:block}
/* nav */
.nav{left:148px;top:118px;width:900px;height:62px;background:var(--teal);display:flex;align-items:center;justify-content:space-between;padding-right:12px;border-bottom:3px solid var(--teal-dark)}
.nav a{flex:none;white-space:nowrap;color:#fff;font-size:15px;padding:0 10px;height:59px;line-height:59px}
.nav a.active{background:var(--teal-dark);padding:0 22px}
/* slider */
.slider{left:148px;top:194px;width:900px;height:405px;background:linear-gradient(120deg,#c9d7a6 0%,#e8c9b0 40%,#9fc3d4 75%,#e2d7b8 100%)}
.slider-caption{position:absolute;left:0;bottom:0;width:100%;height:76px;background:rgba(40,40,40,.55);color:#fff;font-size:19px;font-weight:700;padding:26px 34px;white-space:nowrap}
.slider-arrows{position:absolute;right:8px;bottom:22px;color:#fff;font-size:28px;font-weight:600}
/* headings */
.h-blue{font-size:17px;font-weight:600;color:var(--teal);white-space:nowrap}
.h-orange{font-size:17px;font-weight:600;color:var(--orange);white-space:nowrap}
.body-text{font-size:12px;line-height:22px;color:var(--ink-soft)}
.rule{height:1px;background:var(--rule)}
/* timetable */
.timetable{left:763px;top:917px;width:285px;height:303px;background:var(--sand);border:2px solid #e2d3bf;padding:20px 24px}
.timetable h3{font-size:16px;font-weight:600;color:var(--orange);margin-bottom:12px}
.timetable li{list-style:none;font-size:11px;color:#444;height:30px;line-height:30px;white-space:nowrap}
/* news */
.news-item{top:1329px;width:290px;display:flex;gap:12px}
.date{width:81px;height:94px;background:var(--teal);color:#fff;text-align:center;position:relative;flex:none}
.date b{display:block;font-size:38px;font-weight:600;line-height:50px}
.date span{display:block;font-size:12px;line-height:16px}
.date:after{content:"";position:absolute;right:-8px;top:18px;border:8px solid transparent;border-left-color:var(--teal);border-right:0}
.news-item h4{font-size:13px;font-weight:400;color:var(--teal);margin-bottom:6px;white-space:nowrap}
.news-item p{font-size:11px;line-height:19px;color:var(--ink-soft)}
.pager{display:flex;gap:4px}
.pager i{width:26px;height:26px;border:1px solid #ccc;font-style:normal;font-size:16px;text-align:center;line-height:23px;color:#666}
/* blog */
.post{top:1539px;width:283px;height:271px;background:#f4f4f4}
.post .ph{width:283px;height:207px}
.post-badge{position:absolute;right:0;top:163px;display:flex}
.post-badge .d{width:44px;height:44px;background:var(--teal);color:#fff;text-align:center;font-size:10px;line-height:13px;padding-top:5px}
.post-badge .d b{display:block;font-size:20px;line-height:22px;font-weight:600}
.post-badge .ic{width:44px;height:44px;background:var(--orange)}
.post h4{font-size:14px;font-weight:400;color:var(--teal);text-align:center;margin-top:14px}
.post p{font-size:11px;color:#777;text-align:center;margin-top:6px}
.thumb{width:133px;height:108px}
.show-all{left:769px;top:1789px;width:80px;height:21px;background:var(--teal);color:#fff;font-size:11px;text-align:center;line-height:21px}
/* shop */
.shop{left:148px;top:1885px;width:900px;height:214px;background:var(--cream);border:1px solid #eee5c4;padding:16px 16px;display:flex;gap:16px}
.product{width:205px;height:180px;background:#fff;border:1px solid #e6e6e6}
.product .ph{margin:6px;width:191px;height:128px}
.product p{font-size:11px;color:var(--teal);text-align:center;margin-top:8px}
/* press */
.press{left:148px;top:2186px;width:900px;display:flex;gap:24px}
.press div{width:168px;height:95px;border:1px solid #ccc;display:flex;align-items:center;justify-content:center;font-size:17px;font-weight:700;color:#444;white-space:nowrap}
/* footer */
.footer{left:0;top:2324px;width:1200px;height:251px;background:var(--footer)}
.fcol{top:2366px}
.fcol h5{font-size:17px;font-weight:600;color:var(--orange);padding-bottom:10px;border-bottom:1px solid #444;margin-bottom:14px;white-space:nowrap}
.fcol li{list-style:none;font-size:12px;color:#ccc;line-height:21px}
.tweet{font-size:11px;color:#ccc;line-height:20px}
.contact-row{display:flex;font-size:11px;color:#ccc;line-height:18px;margin-bottom:16px;white-space:nowrap}
.contact-row b{width:74px;font-weight:600;color:#ddd;flex:none}
.bottom{left:0;top:2575px;width:1200px;height:76px;background:var(--footer-deep);color:#ddd;font-size:11px}
.bottom .copy{position:absolute;left:128px;top:30px;white-space:nowrap}
.bottom .copy a{color:var(--orange)}
.bottom .circles{position:absolute;left:932px;top:22px;display:flex;gap:10px}
.bottom .circles i{width:28px;height:28px;border-radius:50%;background:#fff;display:block}
</style>
</head>
<body>
<div class="sheet"></div>

<header>
  <div class="abs brand"><span class="brand-mark"></span><span class="brand-name">Bright Owl</span></div>
  <div class="abs toplinks"><span>The Program</span><span>Class Timetable</span><span>Our Location</span><span>Contact Us</span></div>
  <div class="abs search"><div class="search-field">Keyword</div><div class="search-btn">Search</div></div>
  <div class="abs social"><i style="background:var(--orange)"></i><i style="background:#4d7fc4"></i><i style="background:#2fa9e0"></i></div>
  <nav class="abs nav">
    <a class="active">Home</a><a>The Program »</a><a>Classes »</a><a>Media</a><a>Our Location</a><a>Blog</a><a>About Us »</a><a>Shop</a><a>Contact Us</a>
  </nav>
</header>

<section class="abs slider" role="img" aria-label="Children playing together on cushions outdoors">
  <div class="slider-caption">The Bright Owl Accelerated Learning Centre in Dubai offers</div>
  <div class="slider-arrows">‹ ›</div>
</section>

<section class="welcome">
  <h2 class="abs h-blue" style="left:148px;top:630px">Welcome to Bright Owl!</h2>
  <div class="abs ph" style="left:148px;top:671px;width:193px;height:133px;background:linear-gradient(135deg,#e9c7c0,#c7a6b8 60%,#efe5e0)" role="img" aria-label="Parent and baby during a class"></div>
  <p class="abs body-text" style="left:360px;top:668px;width:688px">Lorem ipsum dolor sit amet, consectetur adipisicing elit. Dicta ducimus numquam quae vodipisicing elit. Dicta ducimus dignissimos, earum iste maxime nam omnis saepe similique! A ad numquam reprehenderit vodipisicing elit. Dicta duci incidunt inventore necessitatibus odio saepe. Lorem ipsum dolor sit amet, consectetur adipisicing elit. Dxcxicta ducim Accusantium ad alias, aliquid aut corporis distinctio dolore eaque esse harum in ipsam dipisicing elit. Dicta ducimuszF nam nihil obcaecati odit omnis reiciendis sed.</p>
  <div class="abs rule" style="left:148px;top:829px;width:900px"></div>
</section>

<section class="features">
  <h2 class="abs h-orange" style="left:148px;top:875px">Bright Owl on Gulf One</h2>
  <div class="abs ph" style="left:148px;top:917px;width:283px;height:193px;background:linear-gradient(160deg,#d9c9c0,#b9c4d4 55%,#e8dcd6)" role="img" aria-label="Video still of a toddler in a striped top">
    <svg width="283" height="193"><circle cx="150" cy="96" r="13" fill="none" stroke="#fff" stroke-width="2"/><path d="M146 89 L156 96 L146 103Z" fill="#fff"/></svg>
  </div>
  <p class="abs body-text" style="left:148px;top:1126px;width:290px;font-size:11px">Bright Owl's Director Layla Haddad is interview on Studio One on the Gulf One TV channel about th Accelerated Learning Program. She talks about brain aining for 6 months up and how the key.</p>

  <h2 class="abs h-orange" style="left:456px;top:875px">Features info about the program</h2>
  <div class="abs ph" style="left:456px;top:917px;width:283px;height:193px;background:linear-gradient(150deg,#8c5a3c,#c58a5c 45%,#3f7fc0 80%,#d14a3a)" role="img" aria-label="Girl at a table with a learning board"></div>
  <p class="abs body-text" style="left:456px;top:1126px;width:290px;font-size:11px">Bright Owl's Director Layla Haddad is interview on Studio One on the Gulf One TV channel about th Accelerated Learning Program. She talks about brain aining for 6 months up and how the key.</p>

  <h2 class="abs h-orange" style="left:763px;top:875px">Class Timetable</h2>
  <div class="abs timetable">
    <h3>Classes by Age Group</h3>
    <ul>
      <li>Babies Class – 6 months – 1 year</li>
      <li>Infants Class – 1 – 2 years</li>
      <li>Toddlers Class – 2 – 3 years</li>
      <li>Minis Class – 3 – 4 years</li>
      <li>Middles Class – 4 – 5 years</li>
      <li>Big Kids Class – 6+ years</li>
      <li>Toddlers Class – 2 – 3 years</li>
      <li>Minis Class – 3 – 4 years</li>
    </ul>
  </div>
</section>

<section class="news">
  <h2 class="abs h-orange" style="left:148px;top:1270px">News and Events</h2>
  <div class="abs pager" style="left:990px;top:1274px"><i>‹</i><i>›</i></div>
  <div class="abs rule" style="left:148px;top:1302px;width:830px"></div>
  <article class="abs news-item" style="left:148px"><div class="date"><b>25</b><span>Jun</span><span>2014</span></div><div><h4>At vero eos et accusamuset</h4><p>At vero eos et accusamuset ius sducimus qui.At vero eos eet iu dignissimosxf.</p></div></article>
  <article class="abs news-item" style="left:468px"><div class="date"><b>25</b><span>Jun</span><span>2014</span></div><div><h4>At vero eos et accusamuset</h4><p>At vero eos et accusamuset ius sducimus qui.At vero eos eet iu dignissimosxf.</p></div></article>
  <article class="abs news-item" style="left:786px"><div class="date"><b>25</b><span>Jun</span><span>2014</span></div><div><h4>At vero eos et accusamuset</h4><p>At vero eos et accusamuset ius sducimus qui.At vero eos eet iu dignissimosxf.</p></div></article>
  <div class="abs rule" style="left:148px;top:1445px;width:900px"></div>
</section>

<section class="blog">
  <h2 class="abs h-orange" style="left:146px;top:1486px">Recent Blog Posts</h2>
  <div class="abs pager" style="left:675px;top:1491px"><i>‹</i><i>›</i></div>
  <div class="abs rule" style="left:148px;top:1522px;width:520px"></div>
  <article class="abs post" style="left:148px">
    <div class="ph" role="img" aria-label="Children drawing together on grass" style="background:linear-gradient(140deg,#9fd06a,#f0d7c4 50%,#7fb7d8)"></div>
    <div class="post-badge"><div class="d">Apr<b>13</b></div><div class="ic"></div></div>
    <h4>Neque porro quisquam est qui.</h4><p>There is no one who by admin, 9 comments</p>
  </article>
  <article class="abs post" style="left:454px">
    <div class="ph" role="img" aria-label="Baby playing under a turquoise cloth" style="background:linear-gradient(140deg,#49c2c8,#8fdde0 50%,#e8d6c8)"></div>
    <div class="post-badge"><div class="d">Apr<b>13</b></div><div class="ic"></div></div>
    <h4>Neque porro quisquam est qui.</h4><p>There is no one who by admin, 9 comments</p>
  </article>

  <h2 class="abs h-orange" style="left:767px;top:1486px">Our Gallery</h2>
  <div class="abs thumb" style="left:769px;top:1537px;background:linear-gradient(135deg,#7fb8d8,#e5b89a)" role="img" aria-label="Gallery photo of hands at play"></div>
  <div class="abs thumb" style="left:915px;top:1537px;background:linear-gradient(135deg,#c9a68a,#9a7ab0)" role="img" aria-label="Gallery photo of a child with a parent"></div>
  <div class="abs thumb" style="left:769px;top:1664px;background:linear-gradient(135deg,#e8c7b0,#c98f6e)" role="img" aria-label="Gallery photo of a child drawing"></div>
  <div class="abs thumb" style="left:915px;top:1664px;background:linear-gradient(135deg,#7a5a4a,#d04a3a 55%,#e8e0d8)" role="img" aria-label="Gallery photo of colourful play blocks"></div>
  <div class="abs show-all">Show All</div>
</section>

<section class="shop-section">
  <h2 class="abs h-orange" style="left:148px;top:1849px">Our Shop</h2>
  <div class="abs shop">
    <div class="product"><div class="ph" style="background:linear-gradient(135deg,#f3f3f3,#d9b27a 50%,#f3f3f3)" role="img" aria-label="Lacing toy set"></div><p>Motor Skills</p></div>
    <div class="product"><div class="ph" style="background:linear-gradient(135deg,#f3f3f3,#4aa06a 45%,#e0643a 70%,#f3f3f3)" role="img" aria-label="Shape puzzle board"></div><p>Motor Skills</p></div>
    <div class="product"><div class="ph" style="background:linear-gradient(135deg,#f3f3f3,#8a86b8 50%,#f3f3f3)" role="img" aria-label="Boxed card game"></div><p>Motor Skills</p></div>
    <div class="product"><div class="ph" style="background:linear-gradient(135deg,#f3f3f3,#3a8ad0 40%,#f0c040 70%,#f3f3f3)" role="img" aria-label="Picture puzzle box"></div><p>Motor Skills</p></div>
  </div>
</section>

<section class="talking">
  <h2 class="abs h-orange" style="left:148px;top:2137px">Who's talking about Bright Owl?</h2>
  <div class="abs pager" style="left:990px;top:2139px"><i>‹</i><i>›</i></div>
  <div class="abs rule" style="left:148px;top:2170px;width:830px"></div>
  <div class="abs press"><div>Daily Seven</div><div>Radio Dune</div><div>The Courier</div><div>Her Edit</div><div>Atelier</div></div>
</section>

<footer>
  <div class="abs footer"></div>
  <div class="abs fcol" style="left:131px;width:180px"><h5>Meta</h5><ul><li>Register</li><li>Log in</li><li>Entries RSS</li><li>Comments RSS</li><li>Blogkit.example</li></ul></div>
  <div class="abs fcol" style="left:357px;width:180px"><h5>Recent Comments</h5><ul><li>Babysitters</li><li>Nannies</li><li>Child</li><li>Housekeepers</li><li>Tutors</li></ul></div>
  <div class="abs fcol" style="left:583px;width:200px"><h5>Latest Tweets</h5>
    <p class="tweet" style="color:#fff;font-weight:600">● Grooming &amp; Spa Services</p>
    <p class="tweet" style="margin-top:8px">Experience the most luxurious and enjoyable pet resort in the Fox Valley, dedicated to the .</p>
    <p class="tweet" style="color:var(--orange);margin-top:14px">http://brightowl.example/</p>
  </div>
  <div class="abs fcol" style="left:853px;width:220px"><h5>Contact Us</h5>
    <div class="contact-row"><b>Address:</b><span>765-85 dummy text fasdf,<br>lorem ipsum Bh7,6<br>6ds usa</span></div>
    <div class="contact-row"><b>Phone:</b><span>+971 555 0100 27</span></div>
    <div class="contact-row"><b>Email:</b><span style="color:var(--orange);font-size:13px">http://brightowl.example/</span></div>
  </div>
  <div class="abs bottom">
    <p class="copy">© Bright Owl Accelerated Learning Centre. All Rights Reserved. &nbsp; <a>About Us</a> &nbsp;|&nbsp; <a>Privacy Policy</a></p>
    <div class="circles"><i></i><i></i><i></i><i></i></div>
  </div>
</footer>
</body>
</html>
```